'Velomar' Nutritional supplements label design (UPDATED)

- 'Velomar' is a upscale health supplements brand
-The company will be packing the products in plastic bottles like other supplements
-Try to use a distinct design which is recognizable from distance
-Brand Logo is attached

-UPDATE- 2-

Label Dimensions and Design:

Hi Everyone,

Sorry for the late response caused by some very busy schedule.

Anyhow, here are the dimensions of the label (Self Adhesive) that we need:

Length of Label : 18cm
Height of Label : 6.5 cm

Product Names:

-Metabolism Formula
-Complete Multivitamins and Minerals (For Men, Women and Kids)
-Healthy Bones
-Skin Support
-Omega-3 oil for Healthy Heart

As for the ingredients just use Lorem Ipsum for now.

Many thanks to all of you in advance.

Target Market(s)

Middle Income families

Industry/Entity Type

Plastic

Requirements
Must have
• -Quality
-Effective
-Unique

```html
<!DOCTYPE html>
<html lang="en">
<head>
<meta charset="utf-8">
<title>Velomar Metabolism Formula Label</title>
<link rel="stylesheet" href="https://fonts.googleapis.com/css2?family=Alfa+Slab+One&family=Arimo:wght@400;700&display=swap">
<style>
  :root {
    --sun-core: #fffbe0;
    --sun-mid: #ffd21a;
    --sun-edge: #ffa800;
    --title-light: #ffb43a;
    --title-dark: #d8560a;
    --title-outline: #8a1a05;
    --capsule-red: #e0120c;
    --badge-yellow: #fff200;
    --ingredient-blue: #1411d6;
    --ink: #111111;
    --brand-teal: #1aa6c4;
    --anatomy-blue: #2a55c8;
    --anatomy-deep: #0f2a8a;
  }
  html, body {
    margin: 0;
    padding: 0;
    overflow: hidden;
    background: #ffffff;
  }
  .label {
    position: relative;
    width: 1200px;
    height: 433px;
    overflow: hidden;
    font-family: "Arimo", Arial, sans-serif;
    background:
      radial-gradient(ellipse 420px 300px at 330px 210px, var(--sun-core) 0%, rgba(255,240,150,0.85) 30%, rgba(255,210,26,0) 75%),
      radial-gradient(ellipse 900px 520px at 330px 210px, var(--sun-mid) 0%, var(--sun-edge) 100%);
  }
  .anatomy-art {
    position: absolute;
    top: 0;
    right: 0;
    width: 330px;
    height: 433px;
    background:
      radial-gradient(ellipse 90px 120px at 150px 120px, rgba(240,170,190,0.85), rgba(240,170,190,0) 100%),
      radial-gradient(ellipse 110px 90px at 140px 300px, rgba(220,140,160,0.8), rgba(220,140,160,0) 100%),
      linear-gradient(90deg, rgba(42,85,200,0) 0%, var(--anatomy-blue) 35%, var(--anatomy-deep) 100%);
  }
  .capsule-count {
    position: absolute;
    left: 150px;
    top: 36px;
    width: 110px;
    text-align: center;
    color: var(--capsule-red);
    font-weight: 700;
  }
  .capsule-count .count {
    display: inline-block;
    background: #ffffff;
    border-radius: 12px;
    padding: 0 8px;
    font-size: 18px;
    line-height: 20px;
  }
  .capsule-count .unit {
    display: block;
    font-size: 19px;
    line-height: 20px;
  }
  .product-title {
    position: absolute;
    left: 380px;
    top: 20px;
    width: 540px;
    height: 290px;
  }
  .product-title text {
    font-family: "Alfa Slab One", Georgia, serif;
    fill: url(#titleFill);
    stroke: var(--title-outline);
    stroke-width: 2.5px;
    paint-order: stroke;
  }
  .ingredient-badge {
    position: absolute;
    left: 398px;
    top: 270px;
    width: 380px;
    height: 76px;
    background: var(--badge-yellow);
    box-sizing: border-box;
    padding: 9px 12px;
  }
  .ingredient-badge span {
    display: block;
    height: 100%;
    background: var(--badge-yellow);
    border: 3px solid #ffffff;
    box-sizing: border-box;
    color: var(--ingredient-blue);
    font-weight: 700;
    font-size: 47px;
    line-height: 52px;
    text-align: center;
  }
  .maker {
    position: absolute;
    left: 62px;
    top: 314px;
    width: 280px;
  }
  .maker .credit {
    display: block;
    text-align: right;
    padding-right: 18px;
    font-size: 12.5px;
    color: var(--ink);
  }
  .maker .brand {
    display: flex;
    align-items: center;
    gap: 10px;
    margin-top: 6px;
    font-weight: 700;
    font-size: 36px;
    letter-spacing: 2px;
    color: var(--brand-teal);
  }
  .maker .brand i {
    width: 28px;
    height: 28px;
    border-radius: 50%;
    background: var(--brand-teal);
  }
  .net-weight {
    position: absolute;
    left: 640px;
    top: 370px;
    font-size: 20px;
    color: var(--ink);
  }
</style>
</head>
<body>
  <main class="label">
    <div class="anatomy-art" role="img" aria-label="Illustration of a translucent human torso showing lungs, liver and digestive organs"></div>

    <div class="capsule-count">
      <span class="count">270</span>
      <span class="unit">Capsules</span>
    </div>

    <svg class="product-title" viewBox="0 0 540 290" aria-label="Metabolism Formula">
      <defs>
        <linearGradient id="titleFill" x1="0" y1="0" x2="0" y2="1">
          <stop offset="0" stop-color="var(--title-light)"/>
          <stop offset="1" stop-color="var(--title-dark)"/>
        </linearGradient>
        <path id="lineOne" d="M25 150 Q250 60 510 100"/>
        <path id="lineTwo" d="M95 258 Q300 210 480 268"/>
      </defs>
      <text font-size="86" textLength="470" lengthAdjust="spacingAndGlyphs"><textPath href="#lineOne">Metabolism</textPath></text>
      <text font-size="86" textLength="380" lengthAdjust="spacingAndGlyphs"><textPath href="#lineTwo">Formula</textPath></text>
    </svg>

    <div class="ingredient-badge"><span>Lorem Ipsum</span></div>

    <div class="maker">
      <span class="credit">Manufactured by:</span>
      <div class="brand"><i></i>VELOMAR</div>
    </div>

    <div class="net-weight">Net Weight 228g(8.0oz)</div>
  </main>
</body>
</html>
```